Business Card for Brenwick Painting

We need a simple, yet out standing business card for our painting company.

Target Market(s)

wealthy; high-end neighborhoods, and businesses

Industry/Entity Type

Painting

Contact Information for Business Card

Name:
Dorian Vask

Email:
d.vask@brenwick-painting.example

Website:
Brenwick-painting.example

Phone Number:
(555) 412-9063

Font styles to use
Serif
Sans Serif

Requirements
Must have
• slogan "making change simple"
Should not have
• A title attached to the name on the card

```html
<!DOCTYPE html>
<html lang="en">
<head>
<meta charset="utf-8">
<title>Brenwick Painting – Business Card</title>
<link rel="stylesheet" href="https://fonts.googleapis.com/css2?family=Lato:wght@400;700&display=swap">
<style>
  :root {
    --bg: #e9e7e4;
    --green-deep: #2a7444;
    --green-dark: #2f5e1e;
    --green-band: #2b6f3a;
    --green-lime: #8dc63f;
    --ink: #222;
    --white: #ffffff;
  }
  * { box-sizing: border-box; margin: 0; padding: 0; }
  html, body { width: 1200px; height: 897px; overflow: hidden; }
  body { background: var(--bg); font-family: "Lato", sans-serif; position: relative; }

  .card {
    position: absolute; left: 290px; width: 620px; height: 354px;
    box-shadow: 0 6px 18px rgba(0,0,0,.18);
    overflow: hidden;
  }

  /* Front */
  .card-front {
    top: 50px;
    background: radial-gradient(ellipse at 60% 20%, #2f8a4d 0%, var(--green-deep) 55%, #23663a 100%);
  }
  .front-brand {
    position: absolute; right: 50px; top: 118px;
    display: flex; align-items: center; gap: 14px;
  }
  .brand-square { width: 34px; height: 34px; background: var(--green-lime); }
  .front-brand .brand-name {
    color: var(--white); font-weight: 700; font-size: 31px; letter-spacing: 2px;
    text-transform: uppercase; line-height: 1.1;
  }
  .slogan {
    position: absolute; right: 70px; top: 236px;
    color: var(--white); font-size: 15px; letter-spacing: 2.2px; text-transform: uppercase;
  }

  /* Back */
  .card-back { top: 470px; background: var(--white); }
  .back-brand {
    position: absolute; left: 38px; top: 130px; width: 240px;
    display: flex; align-items: center; gap: 12px;
  }
  .back-brand .brand-square { width: 30px; height: 30px; }
  .back-brand .brand-name {
    color: var(--green-dark); font-weight: 700; font-size: 24px; letter-spacing: 1.5px;
    text-transform: uppercase; line-height: 1.15;
  }
  .divider { position: absolute; left: 296px; top: 70px; width: 1.5px; height: 190px; background: #333; }
  .contact { position: absolute; left: 335px; top: 66px; color: var(--ink); }
  .contact-name { color: var(--green-band); font-size: 24px; font-weight: 400; margin-bottom: 22px; }
  .contact-address { font-size: 15px; line-height: 1.3; margin-bottom: 24px; }
  .contact-list { list-style: none; font-size: 14.5px; }
  .contact-list li { display: flex; align-items: center; gap: 12px; height: 22px; }
  .contact-list svg { width: 14px; height: 14px; fill: var(--green-band); flex: none; }

  .band-lime { position: absolute; left: 0; bottom: 0; width: 330px; height: 14px; background: var(--green-lime); }
  .band-dark { position: absolute; left: 330px; bottom: 0; right: 0; height: 14px; background: var(--green-band); }
</style>
</head>
<body>

<section class="card card-front" aria-label="Card front">
  <div class="front-brand">
    <span class="brand-square"></span>
    <span class="brand-name">Brenwick Painting</span>
  </div>
  <p class="slogan">Making change simple</p>
</section>

<section class="card card-back" aria-label="Card back">
  <div class="back-brand">
    <span class="brand-square"></span>
    <span class="brand-name">Brenwick Painting</span>
  </div>
  <div class="divider"></div>
  <div class="contact">
    <h1 class="contact-name">Dorian Vask</h1>
    <p class="contact-address">1480 Alder Lane<br>Marlow TX 75000</p>
    <ul class="contact-list">
      <li>
        <svg viewBox="0 0 24 24" aria-hidden="true"><path d="M6.6 10.8a15.1 15.1 0 0 0 6.6 6.6l2.2-2.2a1 1 0 0 1 1-.25 11.4 11.4 0 0 0 3.6.57 1 1 0 0 1 1 1V20a1 1 0 0 1-1 1A17 17 0 0 1 3 4a1 1 0 0 1 1-1h3.5a1 1 0 0 1 1 1c0 1.25.2 2.45.57 3.57a1 1 0 0 1-.25 1z"/></svg>
        (555) 412-9063
      </li>
      <li>
        <svg viewBox="0 0 24 24" aria-hidden="true"><path d="M2 5h20v14H2zm2 2v.5l8 5 8-5V7zm0 2.8V17h16V9.8l-8 5z"/></svg>
        d.vask@brenwick-painting.example
      </li>
      <li>
        <svg viewBox="0 0 24 24" aria-hidden="true"><path d="M12 2a10 10 0 1 0 0 20 10 10 0 0 0 0-20zm6.9 6h-3a15 15 0 0 0-1.3-3.9A8 8 0 0 1 18.9 8zM12 4c.8 1.1 1.5 2.5 1.9 4h-3.8c.4-1.5 1.1-2.9 1.9-4zM4.3 14a8 8 0 0 1 0-4h3.4a16 16 0 0 0 0 4zm.8 2h3a15 15 0 0 0 1.3 3.9A8 8 0 0 1 5.1 16zm3-8h-3a8 8 0 0 1 4.3-3.9A15 15 0 0 0 8.1 8zM12 20c-.8-1.1-1.5-2.5-1.9-4h3.8c-.4 1.5-1.1 2.9-1.9 4zm2.3-6H9.7a14 14 0 0 1 0-4h4.6a14 14 0 0 1 0 4zm.3 5.9a15 15 0 0 0 1.3-3.9h3a8 8 0 0 1-4.3 3.9zm1.7-5.9a16 16 0 0 0 0-4h3.4a8 8 0 0 1 0 4z"/></svg>
        www.brenwick-painting.example
      </li>
    </ul>
  </div>
  <div class="band-lime"></div>
  <div class="band-dark"></div>
</section>

</body>
</html>
```